Painting Company Business Card

Brightwell Painting needs a new business card. See attachments for our logo and current card as an example.
We want to utilize the same colors in the logo, and keep all the information that is currently on it. Just need an updated and modern design.
We are open to loosing the Association Logos if it means a better design.
We are also entertaining a spot for a picture of a headshot of the person listed on the card. Head shot can be finished later.

```html
<!DOCTYPE html>
<html lang="en">
<head>
<meta charset="utf-8">
<title>Brightwell Painting – Business Card</title>
<link rel="stylesheet" href="https://fonts.googleapis.com/css2?family=Montserrat:wght@300;400;600;700&family=Open+Sans:wght@400;600&display=swap">
<style>
  :root {
    --bg: #2b2b2b;
    --card-dark: #1d1d1d;
    --card-light: #ffffff;
    --green: #4b5d3a;
    --maroon: #6d3838;
    --maroon-text: #6a2e2e;
    --photo-grey: #6a6a6a;
    --ink-light: #f2f2f2;
  }
  * { box-sizing: border-box; margin: 0; padding: 0; }
  html, body { width: 1200px; height: 900px; overflow: hidden; }
  body {
    background: var(--bg);
    font-family: "Open Sans", Arial, sans-serif;
    display: flex;
    flex-direction: column;
    align-items: center;
    justify-content: center;
    gap: 30px;
  }
  .card {
    width: 700px;
    height: 400px;
    position: relative;
    overflow: hidden;
    border-radius: 4px;
  }

  /* Back of card */
  .card-back { background: var(--card-dark); }
  .card-back .brand {
    position: absolute;
    top: 120px;
    left: 0; right: 0;
    display: flex;
    align-items: center;
    justify-content: center;
    gap: 16px;
  }
  .brand-square {
    width: 22px; height: 22px;
    background: var(--maroon);
  }
  .brand-name {
    font-family: "Montserrat", Arial, sans-serif;
    font-weight: 700;
    font-size: 46px;
    color: var(--green);
    letter-spacing: 0.5px;
  }
  .services {
    position: absolute;
    top: 262px;
    left: 0; right: 0;
    text-align: center;
    color: var(--ink-light);
    font-size: 17px;
    word-spacing: 1px;
  }
  .services .sep { margin: 0 14px; }

  /* Front of card */
  .card-front { background: var(--card-light); }
  .person {
    position: absolute;
    top: 46px; left: 48px;
    font-family: "Montserrat", Arial, sans-serif;
  }
  .person-name {
    font-size: 28px;
    color: var(--maroon-text);
    letter-spacing: 0.5px;
  }
  .person-name .first { font-weight: 300; }
  .person-name .last { font-weight: 700; }
  .person-title {
    font-size: 15px;
    font-weight: 600;
    color: var(--green);
    margin-top: 2px;
  }
  .person-rule {
    width: 72px; height: 2px;
    background: var(--green);
    margin-top: 4px;
  }
  .card-front .brand {
    position: absolute;
    top: 108px; right: 40px;
    display: flex;
    align-items: center;
    gap: 10px;
  }
  .card-front .brand-name { font-size: 26px; }
  .card-front .brand-square { width: 14px; height: 14px; }
  .contacts {
    position: absolute;
    top: 192px; left: 48px;
    list-style: none;
    color: var(--maroon-text);
    font-size: 17px;
  }
  .contacts li {
    display: flex;
    align-items: center;
    gap: 12px;
    height: 28px;
  }
  .contacts svg { width: 17px; height: 17px; flex: none; }
  .stripe-green {
    position: absolute;
    left: 0; right: 0;
    top: 296px; height: 8px;
    background: var(--green);
  }
  .band-maroon {
    position: absolute;
    left: 0; right: 0;
    top: 316px; bottom: 0;
    background: var(--maroon);
  }
  .headshot {
    position: absolute;
    left: 395px; bottom: 0;
    width: 240px; height: 190px;
    background: linear-gradient(180deg, #767676, var(--photo-grey));
    border-radius: 90px 90px 0 0;
  }
</style>
</head>
<body>

  <section class="card card-back">
    <div class="brand">
      <span class="brand-square"></span>
      <span class="brand-name">Brightwell Painting</span>
    </div>
    <p class="services">
      Exterior Painting<span class="sep">|</span>Interior Painting<span class="sep">|</span>Carpentry<span class="sep">|</span>Drywall
    </p>
  </section>

  <section class="card card-front">
    <div class="person">
      <h1 class="person-name"><span class="first">DANIEL</span> <span class="last">HARPER</span></h1>
      <p class="person-title">QUALITY MANAGER</p>
      <div class="person-rule"></div>
    </div>

    <div class="brand">
      <span class="brand-name">Brightwell Painting</span>
      <span class="brand-square"></span>
    </div>

    <ul class="contacts">
      <li>
        <svg viewBox="0 0 20 20" aria-hidden="true"><path fill="#333" d="M3 7c0-2 3-3 7-3s7 1 7 3v1h-4V6.5H7V8H3zM5 9h10l2 7H3zm5 1.5a2.5 2.5 0 100 5 2.5 2.5 0 000-5z"/></svg>
        <span>262-555-0148</span>
      </li>
      <li>
        <svg viewBox="0 0 20 20" aria-hidden="true"><rect x="2" y="4" width="16" height="12" fill="#333"/><path d="M2.5 4.5L10 11l7.5-6.5" fill="none" stroke="#fff" stroke-width="1.4"/></svg>
        <span>daniel@brightwellpainting.com</span>
      </li>
      <li>
        <svg viewBox="0 0 20 20" aria-hidden="true"><g fill="none" stroke="#555" stroke-width="1.3"><circle cx="10" cy="10" r="7.5"/><ellipse cx="10" cy="10" rx="3.2" ry="7.5"/><path d="M2.5 10h15M4 6h12M4 14h12"/></g></svg>
        <span>BrightwellPainting.com</span>
      </li>
    </ul>

    <div class="stripe-green"></div>
    <div class="band-maroon"></div>
    <div class="headshot" role="img" aria-label="Space for a headshot photo of Daniel Harper"></div>
  </section>

</body>
</html>
```